Looking for an attractive, cool poster design for our company Core Values. This would ideally be framed and placed at each company location. Would like this to be striking and memorable.

The core values that should be included on the poster are:

Be a Creator
Have an Open Mind
Do the Right Thing

The size should be standard poster size, 18 x 24, vertical orientation ideally.

The company name to include on the poster is:

Brightwave Systems Group

The design could be printed as a poster or a sticker/decal as well. Or perhaps printed on a fabric, foam boards. Versatile enough design for different output types.

Target Market(s)

Internal Team Members and visitors

Industry/Entity Type

Technology

Font styles to use
Other font styles liked:
• Montserrat

Requirements
Must have
• The design could be printed as a poster or a sticker/decal as well. Or perhaps printed on a fabric. Versatile enough design for different output types.

```html
<!DOCTYPE html>
<html lang="en">
<head>
<meta charset="utf-8">
<title>Core Values Posters – Brightwave Systems Group</title>
<link rel="stylesheet" href="https://fonts.googleapis.com/css2?family=Oswald:wght@400;500;600;700&family=Stint+Ultra+Condensed&family=Oregano&display=swap">
<style>
  :root {
    --backdrop: #c8c8ca;
    --paper: #e6e3de;
    --mat: #ffffff;
    --ink: #000000;
    --light: #ffffff;
    --shadow: rgba(0, 0, 0, 0.38);
  }
  html, body {
    margin: 0;
    padding: 0;
    width: 1200px;
    height: 559px;
    overflow: hidden;
    background: var(--backdrop);
  }
  .canvas {
    position: relative;
    width: 1200px;
    height: 559px;
  }
  .frame {
    position: absolute;
    top: 54px;
    width: 304px;
    height: 412px;
    padding: 9px;
    background: var(--mat);
    box-shadow: 0 7px 6px -2px var(--shadow);
  }
  .frame--outline { left: 64px; }
  .frame--inverse { left: 439px; }
  .frame--solid { left: 813px; }

  .poster {
    display: block;
    width: 304px;
    height: 412px;
  }

  .heading { font-family: "Stint Ultra Condensed", "Times New Roman", serif; font-size: 37px; }
  .lead { font-family: "Oregano", "Comic Sans MS", cursive; font-size: 18px; }
  .value { font-family: "Oswald", "Arial Narrow", sans-serif; }
  .value--creator { font-size: 58px; font-weight: 500; }
  .value--have { font-size: 35px; font-weight: 500; }
  .value--mind { font-size: 43px; font-weight: 600; }
  .value--do { font-size: 21px; font-weight: 500; }
  .value--thing { font-size: 79px; font-weight: 500; }
  .value--heavy { font-weight: 700; }
  .company { font-family: "Oswald", "Arial Narrow", sans-serif; font-size: 11px; font-weight: 500; letter-spacing: 2px; }

  /* light posters */
  .poster--outline .sheet, .poster--solid .sheet { fill: var(--paper); }
  .poster--outline .ink, .poster--solid .ink { fill: var(--ink); }
  .poster--outline .rule, .poster--solid .rule { stroke: var(--ink); }
  .poster--outline .hollow { fill: none; stroke: var(--ink); stroke-width: 1; }
  .poster--outline .band { fill: var(--ink); }
  .poster--outline .band-text { fill: var(--paper); stroke: var(--ink); stroke-width: 1; }
  .poster--solid .band { fill: var(--ink); }
  .poster--solid .band-text { fill: var(--light); }

  /* dark poster */
  .poster--inverse .sheet { fill: var(--ink); }
  .poster--inverse .ink { fill: var(--light); }
  .poster--inverse .rule { stroke: var(--light); }
  .poster--inverse .hollow { fill: none; stroke: var(--light); stroke-width: 1; }
  .poster--inverse .band { fill: var(--light); }
  .poster--inverse .band-text { fill: var(--light); stroke: var(--ink); stroke-width: 1; }
  .poster--inverse .pill { fill: none; stroke: var(--light); stroke-width: 0.6; }

  .rule { stroke-width: 0.8; }
</style>
</head>
<body>
<main class="canvas">

  <div class="frame frame--outline">
    <svg class="poster poster--outline" viewBox="0 0 304 412" aria-label="Core values poster, outline style">
      <rect class="sheet" width="304" height="412"/>
      <text class="heading ink" x="152" y="44" text-anchor="middle" textLength="113" lengthAdjust="spacingAndGlyphs">CORE VALUES</text>
      <line class="rule" x1="58" y1="96" x2="108" y2="96"/>
      <line class="rule" x1="196" y1="96" x2="248" y2="96"/>
      <text class="lead ink" x="152" y="102" text-anchor="middle" textLength="59" lengthAdjust="spacingAndGlyphs">BE A</text>
      <text class="value value--creator hollow" x="152" y="159" text-anchor="middle" textLength="199" lengthAdjust="spacingAndGlyphs">CREATOR</text>
      <polygon class="band" points="57,196 78,174 223,174 244,196 223,218 78,218"/>
      <text class="value value--have band-text" x="152" y="211" text-anchor="middle" textLength="115" lengthAdjust="spacingAndGlyphs">HAVE AN</text>
      <text class="value value--mind ink" x="152" y="257" text-anchor="middle" textLength="187" lengthAdjust="spacingAndGlyphs">OPEN MIND</text>
      <line class="rule" x1="58" y1="284" x2="89" y2="284"/>
      <line class="rule" x1="211" y1="284" x2="247" y2="284"/>
      <text class="value value--do ink" x="150" y="291" text-anchor="middle" textLength="110" lengthAdjust="spacingAndGlyphs">DO THE RIGHT</text>
      <text class="value value--thing hollow" x="149" y="364" text-anchor="middle" textLength="193" lengthAdjust="spacingAndGlyphs">THING</text>
      <text class="company ink" x="152" y="394" text-anchor="middle">BRIGHTWAVE SYSTEMS GROUP</text>
    </svg>
  </div>

  <div class="frame frame--inverse">
    <svg class="poster poster--inverse" viewBox="0 0 304 412" aria-label="Core values poster, dark style">
      <rect class="sheet" width="304" height="412"/>
      <rect class="pill" x="82" y="16" width="140" height="43" rx="21.5"/>
      <text class="heading ink" x="152" y="49" text-anchor="middle" textLength="113" lengthAdjust="spacingAndGlyphs">CORE VALUES</text>
      <line class="rule" x1="58" y1="96" x2="108" y2="96"/>
      <line class="rule" x1="196" y1="96" x2="248" y2="96"/>
      <text class="lead ink" x="152" y="102" text-anchor="middle" textLength="59" lengthAdjust="spacingAndGlyphs">BE A</text>
      <text class="value value--creator hollow" x="152" y="159" text-anchor="middle" textLength="199" lengthAdjust="spacingAndGlyphs">CREATOR</text>
      <polygon class="band" points="57,196 78,174 223,174 244,196 223,218 78,218"/>
      <text class="value value--have band-text" x="152" y="211" text-anchor="middle" textLength="115" lengthAdjust="spacingAndGlyphs">HAVE AN</text>
      <text class="value value--mind ink" x="152" y="257" text-anchor="middle" textLength="187" lengthAdjust="spacingAndGlyphs">OPEN MIND</text>
      <line class="rule" x1="58" y1="284" x2="89" y2="284"/>
      <line class="rule" x1="211" y1="284" x2="247" y2="284"/>
      <text class="value value--do ink" x="150" y="291" text-anchor="middle" textLength="110" lengthAdjust="spacingAndGlyphs">DO THE RIGHT</text>
      <text class="value value--thing hollow" x="149" y="364" text-anchor="middle" textLength="193" lengthAdjust="spacingAndGlyphs">THING</text>
      <text class="company ink" x="152" y="394" text-anchor="middle">BRIGHTWAVE SYSTEMS GROUP</text>
    </svg>
  </div>

  <div class="frame frame--solid">
    <svg class="poster poster--solid" viewBox="0 0 304 412" aria-label="Core values poster, solid style">
      <rect class="sheet" width="304" height="412"/>
      <text class="heading ink" x="152" y="44" text-anchor="middle" textLength="113" lengthAdjust="spacingAndGlyphs">CORE VALUES</text>
      <line class="rule" x1="58" y1="96" x2="108" y2="96"/>
      <line class="rule" x1="196" y1="96" x2="248" y2="96"/>
      <text class="lead ink" x="152" y="102" text-anchor="middle" textLength="59" lengthAdjust="spacingAndGlyphs">BE A</text>
      <text class="value value--creator value--heavy ink" x="152" y="159" text-anchor="middle" textLength="199" lengthAdjust="spacingAndGlyphs">CREATOR</text>
      <polygon class="band" points="57,196 78,174 223,174 244,196 223,218 78,218"/>
      <text class="value value--have value--heavy band-text" x="152" y="211" text-anchor="middle" textLength="115" lengthAdjust="spacingAndGlyphs">HAVE AN</text>
      <text class="value value--mind ink" x="152" y="257" text-anchor="middle" textLength="187" lengthAdjust="spacingAndGlyphs">OPEN MIND</text>
      <line class="rule" x1="58" y1="284" x2="89" y2="284"/>
      <line class="rule" x1="211" y1="284" x2="247" y2="284"/>
      <text class="value value--do ink" x="150" y="291" text-anchor="middle" textLength="110" lengthAdjust="spacingAndGlyphs">DO THE RIGHT</text>
      <text class="value value--thing value--heavy ink" x="149" y="364" text-anchor="middle" textLength="193" lengthAdjust="spacingAndGlyphs">THING</text>
      <text class="company ink" x="152" y="394" text-anchor="middle">BRIGHTWAVE SYSTEMS GROUP</text>
    </svg>
  </div>

</main>
</body>
</html>
```